Modern Label for cleaning products for the brand Voralux

We need a label design for our line of cleaning products. The label should feature our logo and an image to identify the product's intended use. I've added our logo and an image for use. This only concerns the design of the label on the front of the bottle.

Label dimensions:
Label 1 (500ml bottle with spray): width 58mm x height 115mm
Label 2: (1L bottle): width 73mm x height 140mm
The design must be consistent for both bottles which you find in the pictures.

The bottles to be labeled are white. See the attachment for a photo of the bottles.

The photo must also appear on the label to identify the product's intended use.

Product information:
Brand: Voralux
Product: Sanitary Cleaner

This text must be placed on the label:
"Cleans, descales & freshens. followed with this text: "Ideal for quick and powerful cleaning. A ready-to-use product for everyday use."

- Mention the seperate USP's: Sanitary, Bathroom, Toilet, Wet areas

Appearance: This is a consumer product, but it must have a professional appearance. We would like to see a design that use the color blue from our logo.

Target Market(s)

Consumers who take care of their homes and want to maintain it the correct (professional) way

Font styles to use
Sans Serif

Colors
0054AA
0677BA
7BADD7
CADEEF
E8F1F8

Requirements
Must have
• USP's + use of image and logo + blend in 1 design
Nice to have
• Keep the color of the logo in the design
Should not have
• Comic sans

```html
<!DOCTYPE html>
<html lang="en">
<head>
<meta charset="UTF-8">
<title>Voralux Sanitary Cleaner – Front Label</title>
<link href="https://fonts.googleapis.com/css2?family=Raleway:wght@300;400;600;700&family=Roboto+Condensed:wght@400&display=swap" rel="stylesheet">
<style>
  :root {
    --page-bg: #eef0f2;
    --label-white: #ffffff;
    --brand-blue: #0689d0;
    --deep-blue: #1c45a3;
    --accent-light-blue: #4fa8e8;
    --logo-blue: #0677ba;
    --usp-blue: #0054aa;
    --text-dark: #1a1a1a;
    --photo-light: #e8ecef;
    --photo-mid: #b9bdc0;
    --photo-dark: #7d8185;
  }
  * { margin: 0; padding: 0; box-sizing: border-box; }
  html, body {
    width: 735px;
    height: 1200px;
    overflow: hidden;
    background: var(--page-bg);
  }
  .label {
    position: absolute;
    left: 86px;
    top: 41px;
    width: 563px;
    height: 1117px;
    background: var(--label-white);
    border-radius: 25px;
    overflow: hidden;
    font-family: "Raleway", sans-serif;
  }
  .brand {
    position: absolute;
    left: 0;
    top: 74px;
    width: 100%;
    text-align: center;
  }
  .brand-dot {
    display: block;
    width: 82px;
    height: 82px;
    margin: 0 auto 10px;
    border-radius: 50%;
    background: var(--logo-blue);
  }
  .brand-name {
    font-family: "Raleway", sans-serif;
    font-weight: 700;
    font-size: 40px;
    letter-spacing: 0.5px;
    color: var(--text-dark);
    line-height: 1;
  }
  .usp-list {
    position: absolute;
    left: 0;
    top: 262px;
    width: 100%;
    display: flex;
    justify-content: center;
    gap: 14px;
    list-style: none;
    font-family: "Raleway", sans-serif;
    font-weight: 600;
    font-size: 17px;
    letter-spacing: 1px;
    text-transform: uppercase;
    color: var(--usp-blue);
  }
  .usp-list li + li::before {
    content: "•";
    margin-right: 14px;
    color: var(--accent-light-blue);
  }
  .usage-photo {
    position: absolute;
    left: 0;
    top: 560px;
    width: 100%;
    height: 403px;
    background:
      linear-gradient(90deg, var(--photo-mid) 0%, var(--photo-dark) 18%, var(--photo-mid) 32%, var(--photo-light) 55%, #f6f7f8 75%, var(--photo-mid) 100%);
  }
  .usage-photo::after {
    content: "";
    position: absolute;
    inset: 0;
    background: linear-gradient(180deg, rgba(255,255,255,0.35) 0%, rgba(255,255,255,0) 55%, rgba(150,150,150,0.35) 100%);
  }
  .accent-shapes {
    position: absolute;
    left: 0;
    top: 0;
    width: 563px;
    height: 1117px;
  }
  .title-box {
    position: absolute;
    left: 61px;
    top: 315px;
    width: 441px;
    height: 263px;
    background: var(--brand-blue);
    display: flex;
    flex-direction: column;
    justify-content: center;
    padding-left: 40px;
  }
  .product-title {
    font-family: "Raleway", sans-serif;
    font-weight: 400;
    font-size: 74px;
    line-height: 1.2;
    color: var(--label-white);
    letter-spacing: 0.5px;
  }
  .title-tab {
    position: absolute;
    left: 0;
    top: 487px;
    width: 61px;
    height: 26px;
    background: var(--brand-blue);
  }
  .volume {
    position: absolute;
    left: 30px;
    top: 918px;
    font-size: 22px;
    font-weight: 400;
    color: var(--label-white);
  }
  .info-band {
    position: absolute;
    left: 0;
    top: 963px;
    width: 100%;
    height: 154px;
    background: var(--deep-blue);
    text-align: center;
    padding-top: 22px;
  }
  .claim {
    font-family: "Raleway", sans-serif;
    font-weight: 400;
    font-size: 26px;
    color: var(--accent-light-blue);
    margin-bottom: 10px;
  }
  .usage-line {
    font-family: "Roboto Condensed", sans-serif;
    font-size: 21px;
    line-height: 1.45;
    color: var(--label-white);
  }
</style>
</head>
<body>
  <div class="label">
    <div class="brand">
      <span class="brand-dot"></span>
      <div class="brand-name">voralux</div>
    </div>

    <ul class="usp-list">
      <li>Sanitary</li>
      <li>Bathroom</li>
      <li>Toilet</li>
      <li>Wet areas</li>
    </ul>

    <div class="usage-photo" role="img" aria-label="Photo of a modern bathroom with a glass shower, wall mirror, white vanity unit, tiled bathtub and towel radiator"></div>

    <svg class="accent-shapes" viewBox="0 0 563 1117" aria-hidden="true">
      <polygon points="0,796 161,963 0,963" fill="var(--deep-blue)"/>
      <line x1="496" y1="572" x2="570" y2="654" stroke="var(--brand-blue)" stroke-width="16"/>
    </svg>

    <div class="title-tab"></div>
    <div class="title-box">
      <h1 class="product-title">SANITARY<br>CLEANER</h1>
    </div>

    <div class="volume">500ml</div>

    <div class="info-band">
      <p class="claim">Cleans, Descales &amp; Freshens</p>
      <p class="usage-line">Ideal for quick and powerful cleaning</p>
      <p class="usage-line">A ready-to-use product for everyday use</p>
    </div>
  </div>
</body>
</html>
```